Ridgeline Wild Craft DL flyer

I'm looking for a new flyer for my startup business. In Darwin Australia.
Aimed at family's and short stay tourists the "Ridgeline Wild Craft" 4 hr tour will give people a basic understanding of some essential bush survival skills in the Australian Outback.
things covered in this 4 hr tour are
1. Finding water.
2. finding food.
3. Finding/making shelter and fire.
4. Finding your way home.

The tour will pick clients up in an air conditioned purpose build 4WD and take them to a nearby bushland area where they will have the opportunity to catch and harvest some native bushtucker.
They will then be able to find/harvest some water for survival situations.
While we cook our bush tucker they will also learn to find their way home through ancient navigation techniques as well.

Clients will then be dropped back to their accomodation with some fun and vital knowledge of surviving in the Australian outback.
At the end of the tour the group will be able to take home a basic survival kit which they will be able to use through the skills they just gained on the tour.

I'd like a two sided DL size flyer emphasising the following points.
4hr/half day tour
Fun for the family
Free survival kit included.
Eat what you catch
Learn essential survival skills
Provided buy an experienced and passionate bushman.
$150/head including transfers.

I'll provide some pictures for the flyer and any extra content you require.

Target Market(s)

Family's
Short stay tourists

Industry/Entity Type

Tourism

Colors

Designer to choose colors to be used in the design.

Requirements
Must have
• As per brief
Nice to have
• Any extra content and flair designers would like to add
Should not have
• Any images which aren't Australian

```html
<!DOCTYPE html>
<html lang="en">
<head>
<meta charset="utf-8">
<title>Ridgeline Wild Craft – DL Flyer</title>
<link rel="stylesheet" href="https://fonts.googleapis.com/css2?family=Cinzel:wght@400;500&family=Sorts+Mill+Goudy&display=swap">
<style>
  :root {
    --navy: #1b3562;
    --grey: #5a5c5f;
    --grey-light: #c9cbcd;
    --white: #ffffff;
    --ink: #1d1d1d;
    --page: #ffffff;
    --bush-green: #7d9a4a;
    --bush-sky: #a9c1c9;
    --earth: #a5532b;
    --river: #5e7a4c;
    --skin: #b07a5e;
  }
  * { box-sizing: border-box; margin: 0; padding: 0; }
  html, body { width: 1200px; height: 1051px; overflow: hidden; background: var(--page); }
  body { font-family: "Sorts Mill Goudy", Georgia, serif; color: var(--white); }

  .spread { position: relative; width: 1200px; height: 1051px; display: flex; justify-content: center; align-items: center; gap: 60px; }

  .card { width: 470px; height: 990px; border-radius: 22px; overflow: hidden; display: flex; flex-direction: column; background: var(--navy); box-shadow: 0 4px 14px rgba(0,0,0,.25); }

  .divider { height: 12px; flex: none; background: linear-gradient(90deg, var(--grey) 0%, var(--grey-light) 50%, var(--grey) 100%); }

  .photo { flex: none; }
  .photo--mounds { height: 352px; background: linear-gradient(180deg, var(--bush-sky) 0%, var(--bush-green) 38%, var(--earth) 62%, var(--bush-green) 100%); }
  .photo--catch { flex: 1; background: linear-gradient(160deg, var(--river) 0%, var(--skin) 55%, #4a4a3a 100%); }

  .front-title { height: 250px; flex: none; display: flex; flex-direction: column; align-items: center; justify-content: center; text-align: center; }
  .front-title .tagline { font-size: 29px; margin-bottom: 4px; }
  .brand-title { font-family: "Cinzel", "Times New Roman", serif; font-weight: 500; font-size: 46px; line-height: 1.12; letter-spacing: 1px; }
  .front-title .duration { font-size: 29px; margin-top: 8px; }

  .back-intro { height: 108px; flex: none; display: flex; align-items: center; justify-content: center; text-align: center; font-size: 18px; line-height: 1.45; padding: 0 24px; }

  .photo-row { height: 125px; flex: none; display: flex; gap: 4px; background: var(--white); }
  .photo-row .photo { flex: 1; height: 100%; }
  .photo--shelter { background: linear-gradient(160deg, #cfe0e4, #6f9a4f); }
  .photo--guide { background: linear-gradient(180deg, #e7ebe6, #5d6a4f); }
  .photo--yabby { background: linear-gradient(160deg, #a28968, #4d5a6a); }

  .tour-list { height: 190px; flex: none; display: flex; flex-direction: column; align-items: center; justify-content: center; gap: 6px; font-size: 19px; }
  .tour-list h2 { font-weight: 400; font-size: 17px; margin-bottom: 4px; }
  .tour-list ul { list-style: none; display: flex; flex-direction: column; align-items: center; gap: 6px; }
  .tour-list li { display: flex; align-items: center; gap: 6px; }
  .tick { width: 16px; height: 14px; flex: none; }

  .kit-banner { height: 60px; flex: none; background: var(--grey); display: flex; align-items: center; justify-content: center; font-family: "Sorts Mill Goudy", Georgia, serif; font-size: 25px; letter-spacing: .5px; text-transform: uppercase; }

  .tour-details { height: 232px; flex: none; background: var(--white); color: var(--ink); padding: 14px 18px; font-size: 14.5px; line-height: 1.48; text-align: justify; }
  .tour-details p + p { margin-top: 6px; }

  .back-footer { flex: 1; display: flex; flex-direction: column; align-items: center; justify-content: center; text-align: center; }
  .back-footer .brand-title { font-size: 42px; }
  .back-footer .guide { font-size: 27px; line-height: 1.3; margin-top: 10px; }
  .back-footer .price { font-size: 18px; margin-top: 6px; }
</style>
</head>
<body>
<main class="spread">

  <section class="card card--front" aria-label="Flyer front">
    <div class="photo photo--mounds" role="img" aria-label="Photo of termite mounds among tall grass and gum trees in the outback"></div>
    <div class="divider"></div>
    <header class="front-title">
      <p class="tagline">Fun for the family</p>
      <h1 class="brand-title">RIDGELINE<br>WILD CRAFT</h1>
      <p class="duration">4 hr/half day tour</p>
    </header>
    <div class="divider"></div>
    <div class="photo photo--catch" role="img" aria-label="Photo of the bushman giving a thumbs up while holding a mud crab by a river"></div>
  </section>

  <section class="card card--back" aria-label="Flyer back">
    <p class="back-intro">Understanding of some essential bush survival skills<br>in the Australian Outback</p>
    <div class="divider"></div>
    <div class="photo-row">
      <div class="photo photo--shelter" role="img" aria-label="Photo of a tarp bush shelter on grass"></div>
      <div class="photo photo--guide" role="img" aria-label="Photo of the guide in a wide-brimmed hat"></div>
      <div class="photo photo--yabby" role="img" aria-label="Photo of a freshwater crayfish held in a hand"></div>
    </div>
    <div class="divider"></div>
    <div class="tour-list">
      <h2>Things covered in this 4 hr tour are</h2>
      <ul>
        <li><svg class="tick" viewBox="0 0 16 14"><path d="M1 7.5 L6 12 L15 1.5" fill="none" stroke="currentColor" stroke-width="2.4"/></svg>Finding water.</li>
        <li><svg class="tick" viewBox="0 0 16 14"><path d="M1 7.5 L6 12 L15 1.5" fill="none" stroke="currentColor" stroke-width="2.4"/></svg>Finding food.</li>
        <li><svg class="tick" viewBox="0 0 16 14"><path d="M1 7.5 L6 12 L15 1.5" fill="none" stroke="currentColor" stroke-width="2.4"/></svg>Finding/making shelter and fire.</li>
        <li><svg class="tick" viewBox="0 0 16 14"><path d="M1 7.5 L6 12 L15 1.5" fill="none" stroke="currentColor" stroke-width="2.4"/></svg>Finding your way home.</li>
      </ul>
    </div>
    <div class="kit-banner">Free survival kit included</div>
    <div class="tour-details">
      <p>Our tour will pick you up in an air conditioned purpose build 4WD and take you to a nearby bushland area where you will have the opportunity to catch and harvest some native bushtucker. You will then be able to find/harvest some water for survival situations. While we cook our bush tucker you will also learn to find your way home through ancient navigation techniques as well.</p>
      <p>At the end of the tour the group will be able to take home a basic survival kit which they will be able to use through the skills they just gained on the tour.</p>
    </div>
    <div class="divider"></div>
    <footer class="back-footer">
      <h2 class="brand-title">RIDGELINE<br>WILD CRAFT</h2>
      <p class="guide">Provided by an experienced<br>and passionate bushman.</p>
      <p class="price">$150/head including transfers.</p>
    </footer>
  </section>

</main>
</body>
</html>
```